Velanqua Cookbook (Independant Velanqua Consultant - not Velanqua themselves)

Approx 120 page Recipe book, need design created for recipe pages.
each recipe illustrated with full colour photograph (supplied) on opposite page.
To included index, contents page, intro, etc
Cover design also to be suggested.
We must have a professional finish, but with a friendly, family theme.
Reason: Deadline extended because I require further designs, please.

```html
<!DOCTYPE html>
<html lang="en">
<head>
<meta charset="utf-8">
<title>Red Capsicum &amp; Broccoli Salad</title>
<link rel="stylesheet" href="https://fonts.googleapis.com/css2?family=Rokkitt:wght@300;400&family=Open+Sans:wght@400;600&family=Pinyon+Script&family=Roboto+Condensed:wght@700&display=swap">
<style>
:root {
  --page: #ffffff;
  --ink: #3a3a3a;
  --title: #4b4b4b;
  --muted: #8a8a8a;
  --green: #8cc63f;
  --icon: #9a9a9a;
  --rule: #b5b5b5;
  --photo-mid: #b88a4a;
  --photo-light: #e8e8ea;
}
* { box-sizing: border-box; margin: 0; padding: 0; }
html, body { width: 1200px; height: 681px; overflow: hidden; background: var(--page); }
.spread { position: relative; width: 1200px; height: 681px; background: var(--page); font-family: "Open Sans", sans-serif; color: var(--ink); }

.photo-page { position: absolute; left: 0; top: 0; width: 601px; height: 681px;
  background:
    radial-gradient(ellipse 75% 55% at 48% 70%, #a9803f 0%, #8e6a36 35%, rgba(160,120,70,0) 75%),
    radial-gradient(circle at 10% 12%, #4f7a2a 0%, rgba(79,122,42,0) 22%),
    radial-gradient(circle at 92% 12%, #c2261b 0%, rgba(194,38,27,0) 20%),
    linear-gradient(180deg, var(--photo-light) 0%, #d6d4d0 40%, var(--photo-mid) 100%); }
.spine-label { position: absolute; left: 0; top: 207px; width: 49px; height: 262px; background: var(--page);
  display: flex; align-items: center; justify-content: center; }
.spine-label span { transform: rotate(-90deg); white-space: nowrap; font-family: "Roboto Condensed", sans-serif;
  font-weight: 700; font-size: 13px; color: var(--ink); letter-spacing: 0.2px; }
.page-divider { position: absolute; left: 601px; top: 0; width: 1px; height: 681px; background: #9a9a9a; }

.diet-badge { position: absolute; right: -60px; top: -95px; width: 230px; height: 230px; border-radius: 50%; background: var(--green); }
.diet-list { position: absolute; right: 14px; top: 28px; list-style: none; text-align: right;
  font-family: "Rokkitt", serif; font-size: 11px; line-height: 14px; color: var(--ink); letter-spacing: 0.2px; }
.diet-list li::after { content: " •"; color: #fff; }

.recipe-title { position: absolute; left: 0; top: 0; width: 1200px; height: 0;
  font-family: "Rokkitt", serif; font-weight: 300; font-size: 44px; line-height: 40px;
  color: var(--title); letter-spacing: -1px; }
.recipe-title .line-one, .recipe-title .line-two { position: absolute; white-space: nowrap;
  transform: scaleX(0.82); transform-origin: left top; }
.recipe-title .line-one { left: 690px; top: 163px; }
.recipe-title .line-two { left: 649px; top: 200px; }
.recipe-title .amp { position: absolute; left: 950px; top: 186px; font-family: "Pinyon Script", cursive;
  font-size: 30px; letter-spacing: 0; }

.hero-veg { position: absolute; left: 996px; top: 132px; width: 204px; height: 182px; border-radius: 40% 30% 20% 40%;
  background: radial-gradient(circle at 30% 35%, #4f8a2c 0%, #3d6f22 35%, rgba(61,111,34,0) 60%),
              radial-gradient(circle at 72% 70%, #e3261c 0%, #c41a12 40%, rgba(196,26,18,0) 70%); }

.section-head { position: absolute; top: 297px; display: flex; align-items: center; gap: 6px;
  font-family: "Pinyon Script", cursive; font-weight: 400; font-size: 30px; color: var(--ink); }
.section-head svg { width: 31px; height: 31px; }
.ingredient-head { left: 643px; }
.method-head { left: 851px; }

.column-rule { position: absolute; left: 822px; top: 296px; height: 274px; border-left: 1px dotted var(--rule); }

.ingredients { position: absolute; left: 663px; top: 347px; list-style: none; font-size: 11.5px; font-weight: 600; letter-spacing: -0.3px; }
.ingredients li { height: 29px; }

.method { position: absolute; left: 833px; top: 347px; width: 300px; list-style: none; font-size: 11.5px; font-weight: 600;
  line-height: 15px; letter-spacing: -0.3px; }
.method li { position: relative; padding-left: 8px; margin-bottom: 14px; }
.method li.step::before { content: "•"; position: absolute; left: 0; top: 0; }

.folio { position: absolute; left: 893px; top: 646px; font-size: 11px; color: var(--muted); }
</style>
</head>
<body>
<main class="spread">
  <section class="photo-page" role="img" aria-label="Photograph of chopped red capsicum and broccoli salad with cranberries and almonds in a white dish, garnished with parsley, with broccoli and red peppers behind">
    <div class="spine-label"><span>RED CAPSICUM AND BROCCOLI SALAD</span></div>
  </section>
  <div class="page-divider"></div>

  <section class="recipe-page">
    <div class="diet-badge"></div>
    <ul class="diet-list">
      <li>DAIRY FREE</li>
      <li>EGG FREE</li>
      <li>GLUTEN FREE</li>
    </ul>

    <h1 class="recipe-title">
      <span class="line-one">RED CAPSICUM</span>
      <span class="line-two">BROCCOLI SALAD</span>
      <span class="amp">&amp;</span>
    </h1>
    <div class="hero-veg" role="img" aria-label="Photo of a broccoli head with two red capsicums"></div>

    <h2 class="section-head ingredient-head">
      <svg viewBox="0 0 32 32" aria-hidden="true"><circle cx="16" cy="16" r="16" fill="var(--icon)"/><path d="M9 14h14l-2 8H11z" fill="#fff"/><path d="M12 14l3-5M20 14l-3-5" stroke="#fff" stroke-width="1.6" fill="none"/></svg>
      Ingredient
    </h2>
    <h2 class="section-head method-head">
      <svg viewBox="0 0 32 32" aria-hidden="true"><circle cx="16" cy="16" r="16" fill="var(--icon)"/><rect x="11" y="8" width="8" height="5" rx="2" fill="#fff"/><rect x="12" y="14" width="6" height="10" fill="#fff"/><path d="M20 16l4-3" stroke="#fff" stroke-width="2"/></svg>
      Recipe
    </h2>

    <div class="column-rule"></div>

    <ul class="ingredients">
      <li>3 rashers bacon</li>
      <li>1 red pepper</li>
      <li>½ small red onion</li>
      <li>1 head broccoli</li>
      <li>45g cranberries or sultanas</li>
      <li>30g slivered almonds</li>
      <li>French Dressing</li>
    </ul>

    <ol class="method">
      <li class="step">Chop bacon into large pieces. Pan fry until crisp. Place into Velanqua bowl.</li>
      <li class="cont">Cut red pepper and onion into pieces and add to bowl.</li>
      <li class="step">Chop for 3 seconds on Speed 4.</li>
      <li class="step">Cut broccoli into florets.&nbsp; Add to bowl with cranberries and almonds.</li>
      <li class="step">Chop 5 seconds, Speed 4 or until chopped to desired size.</li>
      <li class="step">Place in serving bowl and drizzle with dressing.</li>
    </ol>

    <div class="folio">01</div>
  </section>
</main>
</body>
</html>
```